All natural lip balm label

Need a label design for a new all natural bath and body company (mybrenvale.com). We provide natural alternatives to harsh bath and body products. We have a lip balm that needs a new design!

I have attached my facebook cover photo because it might help with the design. But you do not have to use that.

Target Market(s)

people 30-55

Industry/Entity Type

It Company

Requirements
Must have
• Name of company is Brena Vale Bath & Body

must have "All Natural Lip Balm" near the logo

Must be in adobe illustrator EPS form (300 dpi) with 4 files (one for each flavor of lip balm: Herbal Mint, Cherry, Vanilla, Peppermint).
See details to art specs on my printer's site: http://www.quorvatags.com/artspecs.htm (note that the text needs to be "outlined")

must be in the following size: 2.125000 x 2.125000 (2-1/8 x 2-1/8)

must have ingredients as shown below...
Ingredients: Organic Glycine Soja (soybean) Oil, Helianthus Annuus (sunflower) Seed Oil, Palm (Elaeis Guineensis) Oil, organic Olea Europaea (Olive) Fruit Oil, Avocado (Persea Gratissima) Oil, Beeswax (Cera Alba), Cocoa (Theobroma Cacao) Seed Butter, Shea Butter (Butyrospermum Parkii), Tocopherol Pure Vitamin E, Natural Flavor

Must have size of product on the label: "0.15 oz/4.25 g"

Must have following verbiage:
distributed by BrenaVale Bath & Body
Dunmere, WI 58407
www.mybrenvale.com

must use the attached logo in some fashion (see "small logo" in attached files)
Nice to have
• use your imagination!

```html
<!DOCTYPE html>
<html lang="en">
<head>
<meta charset="utf-8">
<title>Brena Vale – All natural lip balm labels</title>
<link rel="stylesheet" href="https://fonts.googleapis.com/css2?family=Poiret+One&family=Bodoni+Moda:opsz,wght@6..96,400;6..96,700&display=swap">
<style>
  :root {
    --paper: #ffffff;
    --ink: #222222;
    --brand-green: #0f6b34;
    --edge: #e2e2e2;
    --vanilla: #f8d21a;
    --mint: #6cbd4a;
    --cherry: #e5087e;
    --pepper-red: #e5202a;
    --pepper-orange: #f26b22;
  }
  * { box-sizing: border-box; margin: 0; padding: 0; }
  html, body { width: 1200px; height: 900px; overflow: hidden; background: var(--paper); }
  .sheet { position: relative; width: 1200px; height: 900px; }

  .label {
    position: absolute;
    width: 271px; height: 272px;
    background: var(--paper);
    border-top: 1px solid var(--edge);
    border-bottom: 1px solid var(--edge);
    border-left: 7px solid var(--band-left);
    border-right: 6px solid var(--band-right);
    color: var(--ink);
  }
  .label--vanilla { left: 202px; top: 135px; --band-left: var(--vanilla); --band-right: var(--vanilla); }
  .label--mint    { left: 645px; top: 135px; --band-left: var(--mint); --band-right: var(--mint); }
  .label--cherry  { left: 202px; top: 499px; --band-left: var(--cherry); --band-right: var(--cherry); }
  .label--peppermint { left: 645px; top: 499px; --band-left: var(--pepper-red); --band-right: var(--pepper-orange); }

  .ingredients {
    position: absolute; left: 7px; right: 8px; top: 12px;
    font-family: "Poiret One", sans-serif;
    font-size: 10.4px; line-height: 11.7px;
    text-align: justify; text-align-last: left;
    color: #1a1a1a;
  }

  .brand {
    position: absolute; left: 0; right: 0; top: 114px;
    text-align: center;
    font-family: "Bodoni Moda", serif;
    font-variation-settings: "opsz" 40;
    font-size: 30px; line-height: 36px;
    color: var(--brand-green); font-weight: 400;
  }

  .tagline {
    position: absolute; left: 0; right: 0; top: 159px;
    text-align: center;
    font-family: "Bodoni Moda", serif; font-weight: 700;
    font-variation-settings: "opsz" 20;
    font-size: 12.5px;
  }

  .distributor {
    position: absolute; left: 8px; top: 204px;
    font-family: "Bodoni Moda", serif; font-weight: 400;
    font-variation-settings: "opsz" 60;
    font-size: 9.5px; line-height: 12.7px;
    font-style: normal;
  }

  .flavor-art {
    position: absolute; left: 196px; top: 204px; width: 44px; height: 34px;
    border-radius: 8px;
  }
  .label--vanilla .flavor-art { background: linear-gradient(135deg, #f6e9a4, #4a2f1c); }
  .label--mint .flavor-art { background: radial-gradient(circle, #7cc35a, #3f8f35); }
  .label--cherry .flavor-art { background: radial-gradient(circle at 40% 60%, #e3202a, #8a1016); }
  .label--peppermint .flavor-art { left: 204px; width: 32px; height: 32px; border-radius: 50%; background: radial-gradient(circle, #ffffff 20%, #e5202a 100%); }

  .net-weight {
    position: absolute; right: 20px; top: 244px;
    font-family: "Bodoni Moda", serif; font-weight: 400;
    font-variation-settings: "opsz" 40;
    font-size: 8.5px;
  }
</style>
</head>
<body>
<main class="sheet">

  <section class="label label--vanilla" aria-label="Vanilla lip balm label">
    <p class="ingredients">Ingredients: Organic Glycine Soja (soybean) Oil, Helianthus Annuus (sunflower) Seed Oil, Palm (Elaeis Guineensis) Oil, organic Olea Europaea (Olive) Fruit Oil, Avocado (Persea Gratissima) Oil, Beeswax (Cera Alba), Cocoa (Theobroma Cacao) Seed Butter, Shea Butter (Butyrospermum Parkii), Tocopherol Pure Vitamin E, Natural&nbsp;Flavor</p>
    <p class="brand">Brena Vale</p>
    <p class="tagline">All natural lip balm</p>
    <address class="distributor">Distributed by;<br>BrenaVale Bath &amp; Body<br>Dunmere, WI 58407<br>www.mybrenvale.com</address>
    <div class="flavor-art" role="img" aria-label="Vanilla flower and vanilla bean pods"></div>
    <p class="net-weight">0.15 oz/4.25 g</p>
  </section>

  <section class="label label--mint" aria-label="Herbal mint lip balm label">
    <p class="ingredients">Ingredients: Organic Glycine Soja (soybean) Oil, Helianthus Annuus (sunflower) Seed Oil, Palm (Elaeis Guineensis) Oil, organic Olea Europaea (Olive) Fruit Oil, Avocado (Persea Gratissima) Oil, Beeswax (Cera Alba), Cocoa (Theobroma Cacao) Seed Butter, Shea Butter (Butyrospermum Parkii), Tocopherol Pure Vitamin E, Natural&nbsp;Flavor</p>
    <p class="brand">Brena Vale</p>
    <p class="tagline">All natural lip balm</p>
    <address class="distributor">Distributed by;<br>BrenaVale Bath &amp; Body<br>Dunmere, WI 58407<br>www.mybrenvale.com</address>
    <div class="flavor-art" role="img" aria-label="Sprig of fresh mint leaves"></div>
    <p class="net-weight">0.15 oz/4.25 g</p>
  </section>

  <section class="label label--cherry" aria-label="Cherry lip balm label">
    <p class="ingredients">Ingredients: Organic Glycine Soja (soybean) Oil, Helianthus Annuus (sunflower) Seed Oil, Palm (Elaeis Guineensis) Oil, organic Olea Europaea (Olive) Fruit Oil, Avocado (Persea Gratissima) Oil, Beeswax (Cera Alba), Cocoa (Theobroma Cacao) Seed Butter, Shea Butter (Butyrospermum Parkii), Tocopherol Pure Vitamin E, Natural&nbsp;Flavor</p>
    <p class="brand">Brena Vale</p>
    <p class="tagline">All natural lip balm</p>
    <address class="distributor">Distributed by;<br>BrenaVale Bath &amp; Body<br>Dunmere, WI 58407<br>www.mybrenvale.com</address>
    <div class="flavor-art" role="img" aria-label="Pair of red cherries with a leaf"></div>
    <p class="net-weight">0.15 oz/4.25 g</p>
  </section>

  <section class="label label--peppermint" aria-label="Peppermint lip balm label">
    <p class="ingredients">Ingredients: Organic Glycine Soja (soybean) Oil, Helianthus Annuus (sunflower) Seed Oil, Palm (Elaeis Guineensis) Oil, organic Olea Europaea (Olive) Fruit Oil, Avocado (Persea Gratissima) Oil, Beeswax (Cera Alba), Cocoa (Theobroma Cacao) Seed Butter, Shea Butter (Butyrospermum Parkii), Tocopherol Pure Vitamin E, Natural&nbsp;Flavor</p>
    <p class="brand">Brena Vale</p>
    <p class="tagline">All natural lip balm</p>
    <address class="distributor">Distributed by;<br>BrenaVale Bath &amp; Body<br>Dunmere, WI 58407<br>www.mybrenvale.com</address>
    <div class="flavor-art" role="img" aria-label="Red and white peppermint swirl candy"></div>
    <p class="net-weight">0.15 oz/4.25 g</p>
  </section>

</main>
</body>
</html>
```